Roaming outings business card

please see website
www.roamingoutings.comau

info needed on card
Keiran Voss
Ph
email
Adventure Riding GPS trails

please use my logo and colours off my site

Business

Keiran Voss
keiran@roamingoutings.com

```html
<!DOCTYPE html>
<html lang="en">
<head>
<meta charset="utf-8">
<title>Roaming outings business card</title>
<link rel="stylesheet" href="https://fonts.googleapis.com/css2?family=Russo+One&family=Open+Sans:wght@400&display=swap">
<style>
  :root {
    --canvas: #e9e7e2;
    --card-white: #ffffff;
    --card-black: #111111;
    --ink: #111111;
    --paper: #ffffff;
    --accent-yellow: #f7d51d;
    --accent-yellow-deep: #e9b800;
  }
  * { margin: 0; padding: 0; box-sizing: border-box; }
  html, body { width: 1200px; height: 892px; overflow: hidden; background: var(--canvas); }
  .canvas { position: relative; width: 1200px; height: 892px; }

  .card {
    position: absolute;
    width: 640px;
    height: 366px;
    overflow: hidden;
    box-shadow: 0 10px 26px rgba(0,0,0,0.18);
  }
  .card-back { left: 500px; top: 50px; background: var(--card-black); }
  .card-front { left: 60px; top: 476px; background: var(--card-white); }

  .wordmark {
    position: absolute;
    display: flex;
    align-items: center;
    gap: 18px;
    font-family: "Russo One", sans-serif;
    font-weight: 400;
    text-transform: uppercase;
    line-height: 1;
  }
  .wordmark-mark { display: block; background: var(--accent-yellow); }

  .card-back .wordmark { left: 130px; top: 148px; color: var(--paper); font-size: 48px; }
  .card-back .wordmark-mark { width: 62px; height: 62px; }

  .card-front .wordmark { left: 70px; top: 28px; color: var(--ink); font-size: 40px; }
  .card-front .wordmark-mark { width: 52px; height: 52px; }

  .card-front .edge { position: absolute; inset: 0; }

  .holder-name {
    position: absolute;
    left: 70px;
    top: 140px;
    font-family: "Open Sans", sans-serif;
    font-size: 32px;
    color: var(--ink);
  }
  .divider {
    position: absolute;
    left: 318px;
    top: 140px;
    width: 5px;
    height: 190px;
    background: var(--ink);
  }
  .contact-list {
    position: absolute;
    left: 300px;
    top: 268px;
    list-style: none;
    font-family: "Open Sans", sans-serif;
    font-size: 19px;
    color: var(--ink);
  }
  .contact-list li { display: flex; align-items: center; gap: 14px; height: 28px; }
  .contact-icon { width: 18px; height: 16px; flex: none; }
</style>
</head>
<body>
<main class="canvas">

  <section class="card card-back" aria-label="Card back">
    <div class="wordmark">
      <span class="wordmark-mark"></span>
      <span class="wordmark-name">Roaming outings</span>
    </div>
  </section>

  <section class="card card-front" aria-label="Card front">
    <svg class="edge" viewBox="0 0 640 366" width="640" height="366" aria-hidden="true">
      <polygon points="0,110 60,110 30,210 0,366" fill="var(--card-black)"/>
      <polygon points="0,110 60,110 30,210 10,366 0,366" fill="var(--card-black)"/>
      <polygon points="560,130 640,130 640,300 610,300 590,250 576,190" fill="var(--accent-yellow)"/>
      <polygon points="560,130 600,130 612,190 576,190" fill="var(--accent-yellow-deep)" opacity="0.5"/>
    </svg>

    <div class="wordmark">
      <span class="wordmark-mark"></span>
      <span class="wordmark-name">Roaming outings</span>
    </div>

    <p class="holder-name">Keiran Voss</p>
    <span class="divider"></span>

    <ul class="contact-list">
      <li>
        <svg class="contact-icon" viewBox="0 0 18 16" aria-hidden="true">
          <rect width="18" height="16" fill="var(--ink)"/>
          <polyline points="3,4 9,9 15,4" fill="none" stroke="var(--paper)" stroke-width="1.5"/>
          <rect x="3" y="4" width="12" height="8" fill="none" stroke="var(--paper)" stroke-width="1.2"/>
        </svg>
        <span>keiran@roamingoutings.com</span>
      </li>
      <li>
        <svg class="contact-icon" viewBox="0 0 18 16" aria-hidden="true">
          <rect width="18" height="16" fill="var(--ink)"/>
          <circle cx="9" cy="8" r="5" fill="none" stroke="var(--paper)" stroke-width="1.3"/>
          <line x1="4" y1="8" x2="14" y2="8" stroke="var(--paper)" stroke-width="1"/>
          <ellipse cx="9" cy="8" rx="2.2" ry="5" fill="none" stroke="var(--paper)" stroke-width="1"/>
        </svg>
        <span>www.roamingoutings.com.au</span>
      </li>
    </ul>
  </section>

</main>
</body>
</html>
```